Professional Home Buyer business card needed

I need a pretty straight forward business card designed. We help people that NEED to sell their homes solve problems. We perform all types of Real Estate transactions including flip, wholesale, investment, rental property and multi family. The card will mainly be used to give to prospective Sellers but will also be given to Real Estate Investors as well. It should professional and very easy to read, most clients are older people.

Target Market(s)

Distressed home sellers as well as Real Estate investors

Industry/Entity Type

Real Estate

Contact Information for Business Card

should be a professional layout

Colors
ec1f27
ffffff
000000

Requirements
Must have
• Large logo on back and smaller one on front. should utilize Red, white, and black.
• I am thinking of using a soft touch coating on the card so keep that in mind.
• Contact info should be very easy to read, think older clients.
Nice to have
• I would like to see a design with rounded corners on the card
Should not have
• pictures of homes or other home graphics.

```html
<!DOCTYPE html>
<html lang="en">
<head>
<meta charset="utf-8">
<title>Keystone Home Buyers – Business Card</title>
<link href="https://fonts.googleapis.com/css2?family=Lato:wght@400;700&display=swap" rel="stylesheet">
<style>
  :root {
    --stage: #161616;
    --card: #232323;
    --card-edge: #2c2c2c;
    --red: #ec1f27;
    --white: #ffffff;
    --silver: #9a9a9a;
    --text: #f2f2f2;
  }
  * { box-sizing: border-box; margin: 0; padding: 0; }
  html, body { width: 1200px; height: 912px; overflow: hidden; }
  body {
    background: var(--stage);
    font-family: 'Lato', sans-serif;
    display: flex;
    flex-direction: column;
    align-items: center;
    justify-content: center;
    gap: 28px;
  }
  .card {
    width: 630px;
    height: 360px;
    background: var(--card);
    border: 1px solid var(--card-edge);
    border-radius: 34px;
    position: relative;
  }
  /* back side: large brand */
  .card--back {
    display: flex;
    flex-direction: column;
    align-items: center;
    justify-content: center;
    gap: 44px;
  }
  .brand-large {
    font-weight: 700;
    font-size: 46px;
    letter-spacing: 2px;
    color: var(--silver);
    text-transform: uppercase;
  }
  .website-large {
    font-size: 17px;
    color: var(--text);
    letter-spacing: 0.5px;
  }
  /* front side: small brand + contact */
  .card--front {
    display: flex;
    align-items: center;
  }
  .brand-block {
    width: 300px;
    display: flex;
    align-items: center;
    justify-content: center;
    gap: 10px;
  }
  .brand-mark {
    width: 16px; height: 16px;
    background: var(--red);
  }
  .brand-small {
    font-weight: 700;
    font-size: 24px;
    letter-spacing: 1px;
    color: var(--white);
    text-transform: uppercase;
  }
  .divider {
    width: 2px;
    height: 210px;
    background: var(--red);
  }
  .contact {
    padding-left: 34px;
    color: var(--text);
  }
  .contact__name {
    color: var(--red);
    font-weight: 700;
    font-size: 25px;
  }
  .contact__title {
    font-size: 16px;
    margin-bottom: 18px;
  }
  .contact__address {
    font-size: 16px;
    line-height: 1.35;
    margin-bottom: 16px;
    font-style: normal;
  }
  .contact__list { list-style: none; }
  .contact__list li {
    display: flex;
    align-items: center;
    gap: 12px;
    font-size: 16px;
    line-height: 1.55;
  }
  .contact__list svg { width: 15px; height: 15px; fill: var(--red); flex: none; }
</style>
</head>
<body>

  <section class="card card--back" aria-label="Card back">
    <div class="brand-large">Keystone Home Buyers</div>
    <div class="website-large">www.keystonehomebuyers.com</div>
  </section>

  <section class="card card--front" aria-label="Card front">
    <div class="brand-block">
      <span class="brand-mark"></span>
      <span class="brand-small">Keystone Home Buyers</span>
    </div>
    <div class="divider"></div>
    <div class="contact">
      <div class="contact__name">Daniel Mercer</div>
      <div class="contact__title">Manager</div>
      <address class="contact__address">418 Cedar Brook Lane<br>Austin, TX 78704</address>
      <ul class="contact__list">
        <li>
          <svg viewBox="0 0 24 24"><path d="M6.6 10.8a15.2 15.2 0 0 0 6.6 6.6l2.2-2.2a1 1 0 0 1 1-.25 11.4 11.4 0 0 0 3.6.57 1 1 0 0 1 1 1V20a1 1 0 0 1-1 1A17 17 0 0 1 3 4a1 1 0 0 1 1-1h3.5a1 1 0 0 1 1 1c0 1.25.2 2.45.57 3.57a1 1 0 0 1-.25 1z"/></svg>
          512 555 0142
        </li>
        <li>
          <svg viewBox="0 0 24 24"><path d="M7 3h10v4H7zM4 8h16a2 2 0 0 1 2 2v6h-4v5H6v-5H2v-6a2 2 0 0 1 2-2zm4 7v4h8v-4z"/></svg>
          512 555 0143
        </li>
        <li>
          <svg viewBox="0 0 24 24"><path d="M2 5h20v14H2zm2 2v.5l8 5 8-5V7z"/></svg>
          info@keystonehomebuyers.com
        </li>
        <li>
          <svg viewBox="0 0 24 24"><path d="M12 2a10 10 0 1 0 0 20 10 10 0 0 0 0-20zm6.9 6h-3a15 15 0 0 0-1.3-3.9A8 8 0 0 1 18.9 8zM12 4c.8 1.1 1.5 2.5 1.9 4h-3.8c.4-1.5 1.1-2.9 1.9-4zM4.3 14a8 8 0 0 1 0-4h3.4a16 16 0 0 0 0 4zm.8 2h3a15 15 0 0 0 1.3 3.9A8 8 0 0 1 5.1 16zm3-8h-3a8 8 0 0 1 4.3-3.9A15 15 0 0 0 8.1 8zM12 20c-.8-1.1-1.5-2.5-1.9-4h3.8c-.4 1.5-1.1 2.9-1.9 4zm2.3-6H9.7a14 14 0 0 1 0-4h4.6a14 14 0 0 1 0 4zm.3 5.9a15 15 0 0 0 1.3-3.9h3a8 8 0 0 1-4.3 3.9zm1.7-5.9a16 16 0 0 0 0-4h3.4a8 8 0 0 1 0 4z"/></svg>
          www.keystonehomebuyers.com
        </li>
      </ul>
    </div>
  </section>

</body>
</html>
```